Business Card for Tutoring Company

We need a logo/symbol for an education company, along with an attractive business card. The logo should resemble both a pi symbol and the letter T.
Updates

Dear Designers,

I am narrowing down what I am looking for. 
I want the front of the card to be primarily white, with the company name "Bright Harbor Learning" positioned towards the center.  The first letter, 'T' in 'Bright' will be modified so that it resembles a Pi symbol.
My personal information will be at the bottom.  If you think it fits, the website can be strewn across the top.

As for the back of the card, it will be primarily blue.  Toward the center will be the same T/pi shape engraved into a circular disk/button/emblem shape with some border.  It should be noted that I do like shiny blue, like the blue face of a Varnel.  Underneath the logo will be white text that reads, "Making Independent Learners and Thinkers."  At the very bottom of the card in smaller white font, the website "BrightHarborLearning.example" is written.

For more clarification, see my recent attachment.

Thank you.

Leonard

Industry/Entity Type

Education

Logo styles of interest
Pictorial/Combination Logo
Requirements
Must have
• LOGO:
The logo is a solid blue circle with a symbol cutout from it. The cut out should closely resemble π and be the color white.

CARD:
The front has the logo in the top left corner, with "BRIGHT HARBOR LEARNING" written out beside it, spanning the width of the card. " At the bottom, personal information can be placed: Name, Title, Phone, Email.
The back has the the logo centered and enlarged. The website is printed "BrightHarborLearning.example
Nice to have
• LOGO:
It would be nice if the logo/pi symbol could be used as a letter T when spelling BHL or Bright Harbor Learning.

CARD:
The enlarged logo on the back of the card can be enhanced (i.e. the blue is not solid blue but shiny, like the metallic blue face of a varnel) It would also be nice if the logo had a cool background (i.e. instead of the cutout of the pi-shape being white, it could be outerspace or something. Also, a motto "Making Independent Learner and Thinkers" printed under "BrightHarborLearning.example" would be nice, if it fits.

```html
<!DOCTYPE html>
<html lang="en">
<head>
<meta charset="utf-8">
<title>Bright Harbor Learning – Business Card</title>
<link rel="stylesheet" href="https://fonts.googleapis.com/css2?family=Lobster&family=Tinos:ital,wght@0,400;0,700;1,400&display=swap">
<style>
  :root {
    --ink-blue: #2a2c8f;
    --card-blue: #2d30a0;
    --band-blue: #2f3aa6;
    --band-light: #5a7fd0;
    --paper: #ffffff;
    --backdrop: #e9eaee;
    --glow: #3f63c9;
  }
  html, body {
    margin: 0;
    padding: 0;
    width: 1200px;
    height: 873px;
    overflow: hidden;
    background: var(--backdrop);
  }
  .canvas {
    position: relative;
    width: 1200px;
    height: 873px;
    display: flex;
    align-items: center;
    justify-content: center;
    gap: 40px;
  }
  .card {
    position: relative;
    width: 540px;
    height: 309px;
    border-radius: 4px;
    box-shadow: 0 6px 18px rgba(0,0,0,.18);
    overflow: hidden;
  }

  /* Front */
  .card-front { background: var(--paper); }
  .front-brand {
    position: absolute;
    left: 26px;
    top: 22px;
    display: flex;
    align-items: center;
    gap: 12px;
  }
  .brand-dot {
    width: 46px;
    height: 46px;
    border-radius: 50%;
    background: var(--ink-blue);
  }
  .brand-name {
    font-family: "Lobster", cursive;
    font-size: 42px;
    color: var(--ink-blue);
    line-height: 1;
  }
  .service-band {
    position: absolute;
    left: 0;
    right: 0;
    top: 86px;
    height: 40px;
    background: linear-gradient(180deg, var(--band-light) 0 4px, var(--band-blue) 4px 36px, var(--band-light) 36px);
    display: flex;
    align-items: center;
    padding-left: 40px;
  }
  .service-line {
    font-family: "Tinos", serif;
    font-size: 25px;
    letter-spacing: 1px;
    color: var(--paper);
  }
  .holder {
    position: absolute;
    left: 30px;
    top: 165px;
    font-family: "Tinos", serif;
    color: var(--ink-blue);
  }
  .holder-name { font-weight: 700; font-size: 24px; margin: 0; }
  .holder-title { font-style: italic; font-size: 22px; margin: 6px 0 0; }
  .contact {
    position: absolute;
    right: 28px;
    bottom: 34px;
    font-family: "Tinos", serif;
    font-size: 22px;
    color: var(--ink-blue);
    text-align: right;
  }
  .contact-row {
    display: flex;
    align-items: center;
    justify-content: flex-end;
    gap: 10px;
    margin-top: 10px;
  }
  .contact-row svg { width: 24px; height: 20px; }

  /* Back */
  .card-back {
    background: linear-gradient(135deg, #3236a8 0%, var(--card-blue) 55%, #272a93 100%);
  }
  .emblem-field {
    position: absolute;
    left: 50%;
    top: 54%;
    width: 230px;
    height: 230px;
    transform: translate(-50%, -50%);
    border-radius: 50%;
    background: radial-gradient(circle, #1a2266 0%, #1f3192 38%, var(--glow) 62%, rgba(45,48,160,0) 72%);
  }
  .back-name {
    position: absolute;
    left: 0;
    right: 0;
    top: 30px;
    text-align: center;
    font-family: "Lobster", cursive;
    font-size: 40px;
    color: var(--paper);
  }
  .motto {
    position: absolute;
    left: 0;
    right: 0;
    top: 84px;
    text-align: center;
    font-family: "Tinos", serif;
    font-size: 20px;
    color: var(--paper);
  }
</style>
</head>
<body>
<main class="canvas">
  <section class="card card-front" aria-label="Card front">
    <div class="front-brand">
      <span class="brand-dot"></span>
      <span class="brand-name">Bright Harbor Learning</span>
    </div>
    <div class="service-band">
      <span class="service-line">PREMIER EDUCATION SERVICES</span>
    </div>
    <div class="holder">
      <p class="holder-name">Mara Ellis</p>
      <p class="holder-title">Head Tutor</p>
    </div>
    <div class="contact">
      <div class="contact-row">
        <span>404.555.0182</span>
        <svg viewBox="0 0 24 20" aria-hidden="true"><path d="M8 2 C4 3 3 8 6 13 C9 18 14 19 17 17 L15 13 L12 14 C10 12 9 9 9 7 L12 6 Z" fill="var(--ink-blue)"/></svg>
      </div>
      <div class="contact-row">
        <span>mara.ellis@bhl.example</span>
        <svg viewBox="0 0 24 20" aria-hidden="true"><rect x="1.5" y="3" width="21" height="14" fill="none" stroke="var(--ink-blue)" stroke-width="1.6"/><path d="M1.5 3 L12 11 L22.5 3 M1.5 17 L9 9.5 M22.5 17 L15 9.5" fill="none" stroke="var(--ink-blue)" stroke-width="1.4"/></svg>
      </div>
    </div>
  </section>

  <section class="card card-back" aria-label="Card back">
    <div class="emblem-field" role="img" aria-label="Starry space disk emblem area"></div>
    <div class="back-name">BrightHarborLearning.example</div>
    <div class="motto">Making Independent Learner and Thinkers</div>
  </section>
</main>
</body>
</html>
```